Simple Lawyer Business Card Design Project with gold foil

Looking for a double sided business card. I would like to incorporate two of the images I attached onto the card- a monogram M in a circle and the legal image.
I also added image # 2 as a possibility of how to incorporate both images and for the layout of the information.

Back Side: This side of card will be one version in maroon and one version in white. The logo/vector on back side of card with business name Crandell Legal Group. Shield/Vector should be placed above the Crandell Legal Group lettering in a gold foil press. Please use colors of attachment #3.

Front Side: front of card will be white. front of card could have the monogram M in circle on background (where the lightened scales are on the sample card), with company information over it- Crandell Legal Group. *please delete the crown image above the M* Would like to see the monogram logo in gold -Crandell Legal Group will be in gold foil. Everything on left side should be black font.

Velda Orsini, Esq.
Principal Attorney
Address: 18 Harwick Ave. Suite 212 Woodcliff Lake,
NJ 07419
Phone: 201-739-5186
Fax: 201-826-3947
Email: vorsini@kestrolaw.example
www.kestrolaw.example

Industry/Entity Type

Lawyer

Contact Information for Business Card

Velda Orsini, Esq.
Principal Attorney
Address: 18 Harwick Ave. Suite 212 Woodcliff Lake, NJ 07419
Phone: 201-739-5186
Fax: 201-826-3947
www.kestrolaw.example

Font styles to use
Serif
Other font styles liked:
• fonts on samples

Colors
ffffff

Requirements
Must have
• - The final files must conform w/:
• - https://www.quillpress.example/silk-w-stamped-foil-business-cards
• - https://www.quillpress.example/template-files/business-cards/3.5x2.zip
• - https://www.vidstream.example/watch?v=Q2rTk7LpZxa#action=share
• - we would ask that you upload single page .pdf files only.
• - we recommend a Rich Black value of C=60, M=40, Y=40, K=100
• - Foil mask files are set up just like our Spot UV mask files. The file will only be black and white. The black areas will show where you want the foil placed. White will show areas where you do not want the foil. When ordering a Foil Stamp job with Spot UV, you must provide separate mask files for the Foil (foil mask) and Spot UV (spuv mask). Up to Six files would need to be provided.
• - When using Foil, please keep in mind that Foil and UV can not overlap and we recommend avoiding the use of small/fine text or fonts for foil objects. For best results, please be sure foil coverage is less than 50% of the artwork area.
• - It’s also important to note that there may be up to 1/16" shift on the placement of the foil. Keep this in mind if you are trying to align foil with other printed artwork.
Should not have
• don't want anything cluttered

```html
<!DOCTYPE html>
<html lang="en">
<head>
<meta charset="utf-8">
<title>Crandell Legal Group – Business Card</title>
<link rel="stylesheet" href="https://fonts.googleapis.com/css2?family=Crimson+Text:wght@400;600&family=Open+Sans:wght@400&display=swap">
<style>
  :root {
    --page: #e9e7e4;
    --card-white: #ffffff;
    --card-black: #161616;
    --gold: #b58e46;
    --gold-light: #d2ae68;
    --ink: #1d1d1d;
    --ink-soft: #3a3a3a;
    --rule: #6a6a6a;
    --emboss: #4a4a4a;
  }
  * { margin: 0; padding: 0; box-sizing: border-box; }
  html, body { width: 1200px; height: 1200px; overflow: hidden; background: var(--page); }
  .canvas {
    width: 1200px; height: 1200px;
    display: flex; flex-direction: column; align-items: center; justify-content: center; gap: 60px;
  }
  .card {
    position: relative; width: 840px; height: 480px;
    box-shadow: 0 8px 24px rgba(0,0,0,.18);
  }
  /* Back side */
  .card--back { background: var(--card-black); }
  .back-mark {
    position: absolute; left: 50%; top: 50%; transform: translate(-50%, -50%);
    display: flex; flex-direction: column; align-items: center;
  }
  .back-mark__circle {
    width: 150px; height: 150px; border-radius: 50%;
    background: radial-gradient(circle at 65% 40%, #3a3a3a, #1e1e1e 70%);
  }
  .back-mark__name {
    margin-top: -14px;
    font-family: "Crimson Text", serif; font-size: 56px; font-weight: 400;
    color: var(--emboss); letter-spacing: .5px; white-space: nowrap;
  }
  /* Front side */
  .card--front { background: var(--card-white); }
  .brand {
    position: absolute; left: 90px; top: 130px; width: 380px;
    display: flex; flex-direction: column; align-items: center;
  }
  .brand__circle {
    width: 110px; height: 110px; border-radius: 50%;
    background: radial-gradient(circle at 40% 35%, var(--gold-light), var(--gold) 75%);
  }
  .brand__name {
    margin-top: 10px;
    font-family: "Crimson Text", serif; font-size: 42px; font-weight: 400;
    color: var(--gold); white-space: nowrap;
  }
  .details {
    position: absolute; left: 520px; top: 120px; height: 230px;
    border-left: 2px solid var(--rule); padding-left: 22px;
  }
  .details__name {
    font-family: "Crimson Text", serif; font-size: 30px; font-weight: 400; color: var(--ink);
    line-height: 1;
  }
  .details__title {
    font-family: "Open Sans", sans-serif; font-size: 15px; color: var(--ink-soft); margin-top: 4px;
  }
  .details__address {
    font-family: "Open Sans", sans-serif; font-size: 15px; color: var(--ink-soft);
    margin-top: 14px; line-height: 1.3;
  }
  .contact { list-style: none; margin-top: 12px; }
  .contact__item {
    display: flex; align-items: center; gap: 10px;
    font-family: "Open Sans", sans-serif; font-size: 15px; color: var(--ink-soft); line-height: 1.45;
  }
  .contact__icon { width: 13px; height: 13px; fill: var(--gold); flex: none; }
</style>
</head>
<body>
<main class="canvas">
  <section class="card card--back" aria-label="Card back">
    <div class="back-mark">
      <div class="back-mark__circle"></div>
      <p class="back-mark__name">Crandell Legal Group</p>
    </div>
  </section>

  <section class="card card--front" aria-label="Card front">
    <div class="brand">
      <div class="brand__circle"></div>
      <p class="brand__name">Crandell Legal Group</p>
    </div>

    <div class="details">
      <h1 class="details__name">Velda Orsini, Esq.</h1>
      <p class="details__title">Principal Attorney</p>
      <p class="details__address">18 Harwick Ave. Suite 212<br>Woodcliff Lake, NJ 07419</p>
      <ul class="contact">
        <li class="contact__item">
          <svg class="contact__icon" viewBox="0 0 16 16" aria-hidden="true"><path d="M3.5 1l2.5 3-1.5 1.8c.8 2 2.4 3.6 4.4 4.4L10.7 8.7l3.3 2.4-1 3c-6.5-.3-11.3-5.2-11.6-11.6z"/></svg>
          201-739-5186
        </li>
        <li class="contact__item">
          <svg class="contact__icon" viewBox="0 0 16 16" aria-hidden="true"><path d="M4 1h7l1 1v4H4z M2 6h12a1 1 0 0 1 1 1v5h-3v3H4v-3H1V7a1 1 0 0 1 1-1z M5 11v3h6v-3z"/></svg>
          201-826-3947
        </li>
        <li class="contact__item">
          <svg class="contact__icon" viewBox="0 0 16 16" aria-hidden="true"><path d="M1 3h14v10H1z M1.5 3.5L8 9l6.5-5.5" stroke="#fff" stroke-width="1"/></svg>
          vorsini@kestrolaw.example
        </li>
        <li class="contact__item">
          <svg class="contact__icon" viewBox="0 0 16 16" aria-hidden="true"><circle cx="8" cy="8" r="7"/><path d="M1 8h14M8 1c-3 3.5-3 10.5 0 14M8 1c3 3.5 3 10.5 0 14" stroke="#fff" stroke-width="1" fill="none"/></svg>
          www.kestrolaw.example
        </li>
      </ul>
    </div>
  </section>
</main>
</body>
</html>
```